AUTO SPAREPART DISTRIBUTOR BUSINESS CARD

Our company need a business card design. We are a distributor and importer of car spareparts for ZOVA and MERLOTA car model. We would like the design with White color back ground and attractive color for the fonts and looks clean, simple and attractive.
We provide the company information and the brand logo (ZOVA, MERLOTA, DUP, 738) should be put on the business card.

Thank you

Target Market(s)

Auto spareparts retailer shop and supplier.

Industry/Entity Type

Business

Contact Information for Business Card

The front side of the business card only contain company informations, and the back side may be put the brand logo (ZOVA, MERLOTA, DUP AND 738).

Requirements
Must have
• On the back side ( the brand logo) position , should have a transparency world map picture ( i uploaded the world map picture sample ).
• Also, need to put some words of " AUTO PARTS DISTRIBUTOR " (may be put on any appropriate place).

```html
<!DOCTYPE html>
<html lang="en">
<head>
<meta charset="utf-8">
<title>DUP Auto Parts Distributor – Business Card</title>
<link href="https://fonts.googleapis.com/css2?family=Raleway:wght@200;400;500&display=swap" rel="stylesheet">
<style>
  :root {
    --page: #ecebe8;
    --card: #f7f7f7;
    --card-edge: #e6e6e6;
    --green: #a9cf3c;
    --green-light: #c3e057;
    --ink: #1e1e1e;
    --grey: #6d6d6d;
    --map: #b9b9b9;
    --navy: #1c2f86;
    --red: #c8102e;
  }
  * { margin: 0; padding: 0; box-sizing: border-box; }
  html, body { width: 1200px; height: 1023px; overflow: hidden; }
  body {
    background: var(--page);
    font-family: "Raleway", Arial, sans-serif;
    color: var(--ink);
    position: relative;
  }
  .card {
    position: absolute;
    width: 620px;
    height: 354px;
    border-radius: 18px;
    background: linear-gradient(160deg, #ffffff 0%, var(--card) 60%, var(--card-edge) 100%);
    box-shadow: 0 6px 18px rgba(0,0,0,0.12);
    overflow: hidden;
  }
  .card--front { left: 60px; top: 90px; }
  .card--back { left: 520px; top: 570px; }

  /* front */
  .world-map {
    position: absolute;
    right: 34px; top: 26px;
    width: 250px; height: 118px;
    border-radius: 40px;
    background: radial-gradient(ellipse at center, var(--map) 0%, #d2d2d2 60%, rgba(230,230,230,0) 100%);
  }
  .brand {
    position: absolute;
    left: 70px; top: 166px;
    display: flex; align-items: center; gap: 22px;
  }
  .brand__square { width: 64px; height: 64px; background: var(--green); }
  .brand__name {
    font-weight: 200;
    font-size: 110px;
    letter-spacing: 6px;
    line-height: 1;
    color: var(--ink);
  }
  .tagline {
    position: absolute;
    left: 158px; top: 288px;
    font-size: 17px;
    font-weight: 400;
    letter-spacing: 1px;
    color: var(--green);
  }

  /* back */
  .name-band {
    position: absolute;
    left: 0; top: 22px;
    width: 310px; height: 60px;
    background: var(--green);
    border-radius: 0 30px 30px 0;
    padding: 8px 0 0 150px;
  }
  .name-band__name { font-size: 24px; font-weight: 400; color: #fff; letter-spacing: 1px; line-height: 1; }
  .name-band__role { font-size: 15px; color: var(--ink); margin-top: 4px; }
  .address {
    position: absolute;
    left: 150px; top: 92px;
    font-family: Arial, sans-serif;
    font-size: 14px;
    line-height: 19px;
  }
  .contacts {
    position: absolute;
    left: 118px; top: 140px;
    list-style: none;
    font-family: Arial, sans-serif;
    font-size: 14px;
  }
  .contacts li { display: flex; align-items: center; height: 21px; gap: 12px; }
  .contacts svg { width: 14px; height: 14px; fill: none; stroke: var(--green); stroke-width: 1.4; }
  .partners {
    position: absolute;
    left: 30px; right: 220px; bottom: 26px;
    display: flex; align-items: flex-end; justify-content: space-between;
  }
  .partner { font-size: 22px; font-weight: 500; letter-spacing: 1px; line-height: 1; }
  .partner--merlota { color: var(--navy); }
  .partner--zova { color: var(--red); }
  .partner--738 { color: var(--grey); }
  .back-accent {
    position: absolute;
    right: 40px; bottom: 40px;
    width: 110px; height: 110px;
    background: var(--green-light);
    opacity: 0.25;
  }
</style>
</head>
<body>
  <section class="card card--front" aria-label="Business card front">
    <div class="world-map" role="img" aria-label="Faint grey world map"></div>
    <div class="brand">
      <span class="brand__square"></span>
      <span class="brand__name">DUP</span>
    </div>
    <p class="tagline">AUTO PARTS DISTRIBUTOR</p>
  </section>

  <section class="card card--back" aria-label="Business card back">
    <div class="name-band">
      <p class="name-band__name">RIAN TAN</p>
      <p class="name-band__role">Director</p>
    </div>
    <p class="address">Taman Sari Raya 4, Blok C-07 No.B-18,<br>Kebon Jeruk, Jakarta Barat, Indonesia (11530)</p>
    <ul class="contacts">
      <li><svg viewBox="0 0 14 14"><path d="M3 1h3l1 3-2 1a7 7 0 0 0 4 4l1-2 3 1v3c0 1-1 2-2 2A11 11 0 0 1 1 3c0-1 1-2 2-2z"/></svg>+62-21-58830214</li>
      <li><svg viewBox="0 0 14 14"><rect x="4" y="1" width="6" height="12" rx="1"/><path d="M6 11h2"/></svg>+62-812740396</li>
      <li><svg viewBox="0 0 14 14"><rect x="2" y="5" width="10" height="7"/><path d="M4 5V1h6v4M4 8h6"/></svg>+62-21-58830215</li>
      <li><svg viewBox="0 0 14 14"><rect x="1" y="3" width="12" height="8"/><path d="M1 3l6 5 6-5"/></svg>dup-indonesia@mailbox.com</li>
      <li><svg viewBox="0 0 14 14"><circle cx="7" cy="7" r="6"/><path d="M1 7h12M7 1c-3 3-3 9 0 12M7 1c3 3 3 9 0 12"/></svg>www.dupparts.com</li>
      <li><svg viewBox="0 0 14 14"><circle cx="7" cy="5" r="3"/><path d="M2 13c1-4 9-4 10 0"/></svg>rian.tan27</li>
    </ul>
    <div class="partners">
      <span class="partner partner--merlota">MERLOTA</span>
      <span class="partner partner--zova">ZOVA</span>
      <span class="partner partner--738">738</span>
    </div>
    <div class="back-accent"></div>
  </section>
</body>
</html>
```